SEO AND WEB DESIGN COMPANY BUSINESS CARD DESIGN

I need an eye catching , simple business card design that will match my logo . I need 2 versions of it ( white background and black background) - SOME PEOPLE DID NOT GET IT AND SENDING US FRONT WHITE BACK WHITE VERSIONS WHICH IS NOT CORRECT.

ONE VERSION SHOULD BE BACK AND FRONT ALL BLACK , SECOND VERSION SHOULD BE BACK AND FRONT ALL WHITE

logo psd files are attached for both versions. The business card is going to have : First Name- Last name - position - phone numbers

```html
<!DOCTYPE html>
<html lang="en">
<head>
<meta charset="utf-8">
<title>Northpeak Business Cards – Black Version</title>
<link href="https://fonts.googleapis.com/css2?family=Oswald:wght@400;500&family=Roboto:wght@400;500&display=swap" rel="stylesheet">
<style>
  :root {
    --backdrop: #2a2a2e;
    --card: #0d0d0f;
    --card-edge: #1c1c20;
    --white: #ffffff;
    --blue: #5b93cf;
    --muted: #d9dde3;
  }
  * { box-sizing: border-box; margin: 0; padding: 0; }
  html, body {
    width: 1200px; height: 800px; overflow: hidden;
    background: var(--backdrop);
  }
  .canvas {
    width: 1200px; height: 800px;
    display: flex; align-items: center; justify-content: center; gap: 60px;
  }
  .card {
    width: 510px; height: 292px;
    background: var(--card);
    border-radius: 18px;
    border: 1px solid var(--card-edge);
    position: relative;
    overflow: hidden;
  }

  /* Brand lockup */
  .brand {
    display: flex; align-items: center; gap: 14px;
  }
  .brand-dot {
    width: 30px; height: 30px; border-radius: 50%;
    background: var(--blue);
    flex: none;
  }
  .brand-text { display: flex; flex-direction: column; }
  .brand-name {
    font-family: "Oswald", sans-serif; font-weight: 500;
    color: var(--white); letter-spacing: 1px; line-height: 1;
  }
  .brand-tagline {
    display: flex; align-items: center; gap: 8px;
    font-family: "Roboto", sans-serif; font-size: 8px;
    letter-spacing: 3px; color: var(--muted);
    margin-top: 6px; white-space: nowrap;
  }
  .brand-tagline::before, .brand-tagline::after {
    content: ""; flex: 1; height: 1px; background: var(--blue); min-width: 18px;
  }

  /* Logo side */
  .card-logo { display: flex; align-items: center; justify-content: center; }
  .card-logo .brand-name { font-size: 52px; }

  /* Contact side */
  .card-contact .brand {
    position: absolute; right: 34px; top: 46px;
  }
  .card-contact .brand-name { font-size: 40px; }
  .person {
    position: absolute; right: 34px; top: 128px;
    text-align: right;
  }
  .person-name {
    font-family: "Oswald", sans-serif; font-weight: 500;
    font-size: 28px; color: var(--white); letter-spacing: 1px; line-height: 1.05;
  }
  .person-role {
    font-family: "Oswald", sans-serif; font-weight: 400;
    font-size: 14px; color: var(--blue); letter-spacing: 2.5px;
  }
  .contact-list {
    list-style: none; margin-top: 14px;
    font-family: "Roboto", sans-serif; font-size: 13px; color: var(--white);
  }
  .contact-list li {
    display: flex; align-items: center; justify-content: flex-end; gap: 8px;
    margin-top: 5px;
  }
  .contact-icon { width: 13px; height: 13px; fill: var(--blue); flex: none; }
</style>
</head>
<body>
  <main class="canvas">
    <section class="card card-logo" aria-label="Card back">
      <div class="brand">
        <span class="brand-dot"></span>
        <div class="brand-text">
          <span class="brand-name">NORTHPEAK</span>
          <span class="brand-tagline">DESIGN &amp; MARKETING</span>
        </div>
      </div>
    </section>

    <section class="card card-contact" aria-label="Card front">
      <div class="brand">
        <span class="brand-dot"></span>
        <div class="brand-text">
          <span class="brand-name">NORTHPEAK</span>
          <span class="brand-tagline">DESIGN &amp; MARKETING</span>
        </div>
      </div>
      <div class="person">
        <p class="person-name">DANIEL REYES</p>
        <p class="person-role">MANAGING DIRECTOR</p>
        <ul class="contact-list">
          <li>555-0142-3386
            <svg class="contact-icon" viewBox="0 0 24 24" aria-hidden="true"><path d="M6.6 10.8a15.1 15.1 0 0 0 6.6 6.6l2.2-2.2a1 1 0 0 1 1-.25 11.4 11.4 0 0 0 3.6.57 1 1 0 0 1 1 1V20a1 1 0 0 1-1 1A17 17 0 0 1 3 4a1 1 0 0 1 1-1h3.5a1 1 0 0 1 1 1c0 1.25.2 2.45.57 3.6a1 1 0 0 1-.25 1z"/></svg>
          </li>
          <li>dreyes@northpeak.com
            <svg class="contact-icon" viewBox="0 0 24 24" aria-hidden="true"><path d="M2 5h20v14H2z M2 5l10 8 10-8" fill="var(--blue)"/><path d="M2 5l10 8 10-8" fill="none" stroke="#0d0d0f" stroke-width="1.6"/></svg>
          </li>
        </ul>
      </div>
    </section>
  </main>
</body>
</html>
```